Brightlane Pixel Collective Website

I need my website redesigned to look very modern with the latest services. Check out my old website for information: www.brightlanepixelcollective.com

You can use the same site menu links

It doesn't need to have the Recent News section

Please use the yellow, black and grey color scheme
Updates

This project is now payment guaranteed. Lets see what everyone can do!

Target Market(s)

25-50 years in range. Small Business Owners

Industry/Entity Type

Group

Requirements
Must have
• Logo and similar color scheme to current website
• Modern, Modern, Modern! I want a very fresh and modern look
Should not have
• Boring Look

```html
<!DOCTYPE html>
<html lang="en">
<head>
<meta charset="utf-8">
<title>Brightlane Pixel Collective</title>
<link href="https://fonts.googleapis.com/css2?family=Roboto:wght@300;400;500;700&display=swap" rel="stylesheet">
<style>
:root{
  --accent:#f5b31b;
  --accent-deep:#e09e0a;
  --accent-text:#b97f00;
  --on-accent:#141414;
  --nav:#676b78;
  --hero-panel:#7f8b98;
  --card-light:#a1aab5;
  --card-dark:#656874;
  --tab-bar:#9ba3ae;
  --tab-active:#c8cdd4;
  --panel-bg:#f6f7f9;
  --text:#6a6d75;
  --heading:#5f636d;
  --footer:#636672;
  --footer-dark:#555863;
  --rule:#d7d9dd;
  --white:#ffffff;
  --black:#0b0b0b;
}
*{margin:0;padding:0;box-sizing:border-box}
html,body{width:990px;height:1200px;overflow:hidden;background:#fff}
body{position:relative;font-family:"Roboto",Arial,sans-serif;color:var(--text);font-size:8px;line-height:1.35}
.abs{position:absolute}
a{color:inherit;text-decoration:none}

/* header */
.logo{left:133px;top:7px;width:105px;height:61px;background:var(--black);display:flex;flex-direction:column;align-items:center;justify-content:center;gap:6px}
.logo-mark{width:16px;height:16px;background:var(--accent)}
.logo-name{color:var(--white);font-size:8px;font-weight:400;text-align:center;line-height:1.15;letter-spacing:.3px;text-transform:uppercase}
.social-top{left:645px;top:31px;display:flex;gap:10px;align-items:center}
.dot{width:10px;height:10px;border-radius:50%;background:#7c808a}
.sep{left:760px;top:32px;width:1px;height:9px;background:#c9ccd1}
.top-links{left:778px;top:32px;display:flex;gap:10px;font-size:7.5px;color:#5f636d}

/* nav */
.nav{left:133px;top:74px;width:724px;height:37px;background:var(--nav);box-shadow:0 8px 10px -6px rgba(0,0,0,.35)}
.nav-home{left:0;top:0;width:38px;height:37px;background:#5d616d;display:flex;align-items:center;justify-content:center}
.nav-links{left:62px;top:0;height:37px;display:flex;align-items:center;color:var(--white);font-size:8.5px}
.nav-links span{margin-right:26px}
.nav-search{right:0;top:0;width:38px;height:37px;background:var(--accent);display:flex;align-items:center;justify-content:center}

/* hero */
.hero-photo{left:133px;top:130px;width:539px;height:309px;background:linear-gradient(100deg,#c9d3dc 0%,#dfe6ec 40%,#b9c6d3 75%,#d4dde6 100%)}
.hero-panel{left:672px;top:130px;width:185px;height:309px;background:var(--hero-panel);padding:18px 18px;color:var(--white)}
.kicker{font-weight:300;font-size:15px;line-height:1.1;text-transform:uppercase}
.strong{font-weight:700;font-size:15px;line-height:1.15;text-transform:uppercase}
.blurb{font-size:7.8px;font-weight:400;line-height:1.4;margin-top:9px;max-width:146px}
.btn{display:inline-flex;align-items:center;gap:8px;background:var(--accent);color:var(--on-accent);font-weight:700;font-size:7px;text-transform:uppercase;padding:0 10px;height:24px}
.plus{font-size:12px;font-weight:700;line-height:1}

/* feature cards */
.card-photo{top:458px;width:167px;height:148px}
.card-panel{top:458px;width:186px;height:148px;padding:16px 18px;color:var(--white)}

/* tabs */
.tabs{left:133px;top:625px;width:353px;height:228px;background:var(--panel-bg)}
.tab-bar{left:0;top:0;width:353px;height:43px;background:var(--tab-bar);display:flex}
.tab{width:70.6px;height:43px;display:flex;align-items:center;justify-content:center}
.tab.active{background:var(--tab-active)}
.tab-title{left:17px;top:60px;font-size:15px;font-weight:700;color:var(--heading);text-transform:uppercase}
.tab-copy{left:18px;top:86px;width:318px;font-size:7.6px;line-height:1.36;color:var(--text)}
.tab-copy p+p{margin-top:10px}

/* section heads */
.section-head{top:622px;font-size:15px;font-weight:700;color:var(--heading);text-transform:uppercase}
.pager{top:629px;display:flex;gap:2px}
.pager i{width:4px;height:4px;border-radius:50%;background:#a8adb5}
.pager i:last-child{background:var(--accent)}

/* latest post */
.post{left:503px;width:169px;height:40px;border-bottom:1px solid var(--rule)}
.post-thumb{left:1px;top:1px;width:31px;height:32px;background:linear-gradient(135deg,#cfd6de,#8e9aa8)}
.post-title{left:38px;top:0;font-size:7.2px;color:var(--accent-text);font-weight:500}
.post-text{left:38px;top:10px;width:132px;font-size:6.8px;line-height:1.3;color:var(--text)}
.all-post{left:601px;top:827px;width:71px;height:25px;justify-content:center}

/* recent works */
.work{left:689px;width:168px}
.work-photo{background:linear-gradient(120deg,#e6ebef,#9eabb9)}
.work-accent{top:723px;height:61px;background:var(--accent);color:var(--on-accent);display:flex;flex-direction:column;align-items:center;justify-content:center;gap:4px;font-size:7px;font-weight:700;text-transform:uppercase}

/* news */
.news{top:870px;width:107px}
.news-date{font-size:14px;font-weight:500;color:var(--heading);line-height:1;padding-bottom:5px;border-bottom:3px solid var(--rule)}
.news-date small{font-size:8px;font-weight:700;text-transform:uppercase}
.news-title{margin-top:11px;font-size:8px;font-weight:700;color:#55585f;text-transform:uppercase}
.news-text{margin-top:2px;font-size:6.8px;line-height:1.3;color:var(--text)}
.news-more{margin-top:4px;font-size:6.8px;font-weight:500;color:var(--accent-text)}

/* tweet band */
.tweet-band{left:0;top:1035px;width:990px;height:25px;background:var(--accent);color:var(--on-accent)}
.tweet-dot{left:134px;top:7px;width:11px;height:11px;border-radius:50%;background:var(--on-accent)}
.tweet-text{left:159px;top:7px;font-size:7.8px}
.tweet-text b{font-weight:700}
.tweet-nav{top:0;width:24px;height:25px;display:flex;align-items:center;justify-content:center}

/* footer */
.footer{left:0;top:1060px;width:990px;height:116px;background:var(--footer);color:var(--white)}
.foot-title{left:133px;top:34px;font-size:16px;font-weight:700;text-transform:uppercase;line-height:1}
.foot-sub{left:133px;top:50px;font-size:6.8px}
.foot-social{left:133px;top:69px;display:flex;gap:13px}
.foot-social .dot{background:var(--white);width:12px;height:12px}
.foot-links{right:133px;top:54px;display:flex;gap:18px;font-size:7.4px}
.copyright{left:0;top:1176px;width:990px;height:24px;background:var(--footer-dark);color:var(--white);font-size:6.4px;padding:8px 0 0 133px}
</style>
</head>
<body>

<header>
  <div class="abs logo">
    <div class="logo-mark"></div>
    <div class="logo-name">Brightlane Pixel<br>Collective</div>
  </div>
  <div class="abs social-top" aria-label="Social links">
    <span class="dot"></span><span class="dot"></span><span class="dot"></span><span class="dot"></span><span class="dot"></span>
  </div>
  <div class="abs sep"></div>
  <nav class="abs top-links"><a>News</a><a>FAQ</a><a>Contact</a></nav>
</header>

<nav class="abs nav">
  <div class="abs nav-home">
    <svg width="13" height="12" viewBox="0 0 13 12"><path d="M6.5 0 0 5.5h2V12h3.5V8h2v4H11V5.5h2z" fill="#fff"/></svg>
  </div>
  <div class="abs nav-links">
    <span>About</span><span>Portfolio</span><span>Blog</span><span>Technology</span><span>What We Do</span><span>Aproch</span><span>Contact</span>
  </div>
  <div class="abs nav-search">
    <svg width="12" height="12" viewBox="0 0 12 12"><circle cx="5" cy="5" r="3.6" fill="none" stroke="#141414" stroke-width="1.8"/><path d="M7.6 7.6 11 11" stroke="#141414" stroke-width="2"/></svg>
  </div>
</nav>

<section>
  <div class="abs hero-photo" role="img" aria-label="Smiling businessman in a light office with colleagues blurred in the background"></div>
  <div class="abs hero-panel">
    <div class="kicker">Responsive Design</div>
    <div class="strong">Buy Now</div>
    <p class="blurb">Lorem ipsum dolor sit amet, consectetur adipisicing elit, sed do eiusmod tempor incididunt ut labore et dolore magna aliqua.</p>
    <div style="margin-top:18px"><span class="btn">All Post <span class="plus">+</span></span></div>
  </div>
</section>

<section>
  <div class="abs card-photo" style="left:133px;background:linear-gradient(120deg,#b8c3cf,#5b6778)" role="img" aria-label="Business partners shaking hands at a meeting table"></div>
  <div class="abs card-panel" style="left:300px;background:var(--card-light)">
    <div class="kicker">Marketing Sors</div>
    <div class="strong">Start Now</div>
    <p class="blurb">Lorem ipsum dolor sit amet, consectetur adipisicing elit, sed do eiusmod tempor incididunt ut labore et dolore magna aliqua.</p>
  </div>
  <div class="abs card-photo" style="left:504px;background:linear-gradient(120deg,#e3e7eb,#9aa4ae)" role="img" aria-label="Two colleagues working at a laptop, one on the phone"></div>
  <div class="abs card-panel" style="left:671px;background:var(--card-dark)">
    <div class="kicker">Branding</div>
    <div class="strong">Start Now</div>
    <p class="blurb">Lorem ipsum dolor sit amet, consectetur adipisicing elit, sed do eiusmod tempor incididunt ut labore et dolore magna aliqua.</p>
  </div>
</section>

<section class="abs tabs">
  <div class="abs tab-bar">
    <div class="tab"><svg width="22" height="16" viewBox="0 0 22 16"><g fill="#fff"><rect x="1" y="10" width="3" height="6"/><rect x="6" y="7" width="3" height="9"/><rect x="11" y="9" width="3" height="7"/><rect x="16" y="4" width="3" height="12"/></g><path d="M1 8 7 3l5 3 8-5" stroke="#fff" stroke-width="1.4" fill="none"/></svg></div>
    <div class="tab"><svg width="24" height="16" viewBox="0 0 24 16"><rect x="4" y="1" width="16" height="11" fill="none" stroke="#fff" stroke-width="1.6"/><path d="M1 14h22v1.5H1z" fill="#fff"/></svg></div>
    <div class="tab active"><svg width="18" height="18" viewBox="0 0 18 18" stroke="#fff" stroke-width="1.6" fill="none"><path d="M1 6V1h5M1 1l5 5M17 6V1h-5M17 1l-5 5M1 12v5h5M1 17l5-5M17 12v5h-5M17 17l-5-5"/></svg></div>
    <div class="tab"><svg width="20" height="20" viewBox="0 0 20 20"><path d="M1 9a9 8 0 0 1 18 0c-2-1-3-1-4.5 0-1.5-1-3-1-4.5 0-1.5-1-3-1-4.5 0C4 8 3 8 1 9z" fill="#fff"/><path d="M10 9v8a2 2 0 0 1-4 0" stroke="#fff" stroke-width="1.5" fill="none"/></svg></div>
    <div class="tab"><svg width="26" height="20" viewBox="0 0 26 20"><circle cx="9" cy="11" r="8" fill="#fff"/><circle cx="19" cy="6" r="6" fill="#fff"/><text x="9" y="15" font-size="11" font-weight="700" text-anchor="middle" fill="#9ba3ae" font-family="Arial,sans-serif">?</text></svg></div>
  </div>
  <h2 class="abs tab-title">Responsive Design</h2>
  <div class="abs tab-copy">
    <p>Lorem ipsum dolor sit amet, consectetur adipisicing elit, sed do eiusmod tempor incididunt ut labore et dolore magna aliqua. Ut enim ad minim veniam, quis nostrud exercitation ullamco laboris .</p>
    <p>At vero eos et accusamus et iusto odio dignissimos ducimus qui blanditiis praesentium voluptatum deleniti atque corrupti quos dolores et quas molestias excepturi sint occaecati cupiditate non provident, similique sunt in culpa qui officia deserunt mollitia distinctio. Nam libero tempore, cum soluta nobis est eligendi optio voluptas assumenda est, omnis dolor repellendus.</p>
  </div>
</section>

<section>
  <h2 class="abs section-head" style="left:503px">Latest Post</h2>
  <div class="abs pager" style="left:654px"><i></i><i></i><i></i></div>

  <article class="abs post" style="top:654px"><div class="abs post-thumb" role="img" aria-label="Office team photo"></div><div class="abs post-title">Company Aurelence</div><p class="abs post-text">Lorem ipsum dolor sit amet, consectetur adipisicing elit, sed do.</p></article>
  <article class="abs post" style="top:697px"><div class="abs post-thumb" role="img" aria-label="Business meeting photo"></div><div class="abs post-title">Stock Runing</div><p class="abs post-text">Lorem ipsum dolor sit amet, consectetur adipisicing elit, sed do.</p></article>
  <article class="abs post" style="top:741px"><div class="abs post-thumb" role="img" aria-label="Team at a desk photo"></div><div class="abs post-title">Morning Shines Reboot</div><p class="abs post-text">Lorem ipsum dolor sit amet, consectetur adipisicing elit, sed do.</p></article>
  <article class="abs post" style="top:784px;border-bottom:0"><div class="abs post-thumb" role="img" aria-label="Colleagues portrait photo"></div><div class="abs post-title">My protest Paid</div><p class="abs post-text">Lorem ipsum dolor sit amet, consectetur adipisicing elit, sed do.</p></article>
  <span class="abs btn all-post">All Post <span class="plus">+</span></span>

  <h2 class="abs section-head" style="left:689px">Recent Works</h2>
  <div class="abs pager" style="left:839px"><i></i><i></i><i></i></div>
  <div class="abs work work-photo" style="top:654px;height:62px" role="img" aria-label="Group of business people standing together"></div>
  <div class="abs work work-accent">Lumen Theme<span class="plus">+</span></div>
  <div class="abs work work-photo" style="top:790px;height:63px" role="img" aria-label="Business people at a meeting table"></div>
</section>

<section>
  <article class="abs news" style="left:133px"><div class="news-date">29 <small>May</small></div><h3 class="news-title">Good Idea</h3><p class="news-text">Duis aute irure dolor inserar reprehenderit in voluptate velit esse cillum dolore eu fugiat pariatur relased.</p><div class="news-more">read more</div></article>
  <article class="abs news" style="left:257px"><div class="news-date">28 <small>May</small></div><h3 class="news-title">Avasome Design</h3><p class="news-text">Duis aute irure dolor inserar reprehenderit in voluptate velit esse cillum dolore eu fugiat pariatur relased.</p><div class="news-more">read more</div></article>
  <article class="abs news" style="left:380px"><div class="news-date">27 <small>May</small></div><h3 class="news-title">Perfect Pixels</h3><p class="news-text">Duis aute irure dolor inserar reprehenderit in voluptate velit esse cillum dolore eu fugiat pariatur relased.</p><div class="news-more">read more</div></article>
  <article class="abs news" style="left:504px"><div class="news-date">26 <small>May</small></div><h3 class="news-title">Unique Colurs</h3><p class="news-text">Duis aute irure dolor inserar reprehenderit in voluptate velit esse cillum dolore eu fugiat pariatur relased.</p><div class="news-more">read more</div></article>
  <article class="abs news" style="left:628px"><div class="news-date">25 <small>May</small></div><h3 class="news-title">Easy Editable</h3><p class="news-text">Duis aute irure dolor inserar reprehenderit in voluptate velit esse cillum dolore eu fugiat pariatur relased.</p><div class="news-more">read more</div></article>
  <article class="abs news" style="left:751px"><div class="news-date">24 <small>May</small></div><h3 class="news-title">Layered PSD</h3><p class="news-text">Duis aute irure dolor inserar reprehenderit in voluptate velit esse cillum dolore eu fugiat pariatur relased.</p><div class="news-more">read more</div></article>
</section>

<div class="abs tweet-band">
  <span class="abs tweet-dot"></span>
  <p class="abs tweet-text">Nam libero tempore, cum soluta nobis est eligendi optio cumque nihil impedit quo minus id quod maxime placeat facere possimus, omnis voluptas <b>@pixelcollective</b></p>
  <div class="abs tweet-nav" style="left:808px"><svg width="6" height="8" viewBox="0 0 6 8"><path d="M5 1 2 4l3 3" stroke="#141414" stroke-width="1.6" fill="none"/></svg></div>
  <div class="abs tweet-nav" style="left:832px;background:var(--accent-deep)"><svg width="6" height="8" viewBox="0 0 6 8"><path d="M1 1l3 3-3 3" stroke="#141414" stroke-width="1.6" fill="none"/></svg></div>
</div>

<footer class="abs footer">
  <h2 class="abs foot-title">Get In Touch</h2>
  <p class="abs foot-sub">Lorem ipsum dolor sit amet, consectetur adipisicing</p>
  <div class="abs foot-social" aria-label="Social links"><span class="dot"></span><span class="dot"></span><span class="dot"></span><span class="dot"></span><span class="dot"></span><span class="dot"></span></div>
  <nav class="abs foot-links"><a>Home</a><a>Pages</a><a>Portfolio</a><a>Shortcodes</a><a>Features</a><a>Blog</a><a>Contact</a></nav>
</footer>
<div class="abs copyright">Copyright 2013 Northfield Studio</div>

</body>
</html>
```